Business card design needed

Want the logo on a medium blue background and a nice funky design. I have my own gym and run one on one personal training and nutrition sessions. want it to look lively.
Updates

Please note I requested my logo on a blue background 

PLEASE NOTE: I already have a logo. It is attached to the order!!

Target Market(s)

over 55s

Industry/Entity Type

Nutrition

Contact Information for Business Card

Front of card : Logo ( on blue background )
Corinne Dalby
Nutrition & Fitness Coach for Seniors
Private gym at : 17 Fennick Street, Brantwood, Perth, WA 6291
Mob : 0412736158
Email : corinnedalby@fernpost.example
"For Seniors by a Senior"

Back of card
B.A. ( Soc.)
Dip. Ed. (Sec.)
Wellness Coach
Cert 4 Personal Trainer
Cert. Nutritition
MOVE ON Facilitator
Ageing Well Moving Freely Facilitator
NLP Master

```html
<!DOCTYPE html>
<html lang="en">
<head>
<meta charset="utf-8">
<title>Evergreen Years – Business Cards</title>
<link rel="stylesheet" href="https://fonts.googleapis.com/css2?family=Fira+Sans:ital,wght@0,400;0,600;0,700;1,600;1,700&family=Alegreya:ital,wght@1,700&display=swap">
<style>
:root{
  --sky:#0aa6e6;
  --navy:#0d4f82;
  --deep:#0a3f6b;
  --ink:#124a78;
  --sun:#f3e10f;
  --white:#ffffff;
  --rule:#4fb7e6;
  --stage:#eef1f4;
}
*{box-sizing:border-box;margin:0;padding:0}
html,body{width:1200px;height:1058px;overflow:hidden}
body{background:var(--stage);position:relative;font-family:"Fira Sans",Arial,sans-serif;color:var(--ink)}
.card{position:absolute;width:514px;height:284px;border-radius:14px;overflow:hidden;background:var(--white);box-shadow:0 4px 10px rgba(0,0,0,.18)}
.card--back{left:339px;top:47px;width:514px;height:283px;background:linear-gradient(160deg,#1b6f9c,#0d4f7a 60%,#0b456e)}
.card--a{left:60px;top:384px}
.card--b{left:626px;top:384px}
.card--c{left:62px;top:719px}
.card--d{left:626px;top:719px}
.swoosh{position:absolute;left:0;top:0;width:514px;height:284px}
.brand{position:absolute;color:var(--white);font-weight:600;line-height:1.15}
.brand__dot{display:inline-block;width:14px;height:14px;border-radius:50%;background:var(--sun);vertical-align:middle;margin-right:6px}
.brand--front{left:32px;top:98px;font-size:23px;width:210px}
.brand--front .brand__sub{font-size:18px}
.tagline{position:absolute;font-style:italic;font-weight:700;color:var(--ink);font-size:14px}
.addr{position:absolute;text-align:right;color:var(--sky);font-size:11.5px;line-height:1.3}
.name{position:absolute;font-weight:700;color:var(--ink);font-size:24px;white-space:nowrap}
.role{position:absolute;color:var(--sky);font-size:13px;text-align:right;line-height:1.3}
.rule{position:absolute;height:1px;background:var(--rule)}
.contact{position:absolute;text-align:right;font-weight:600;color:var(--ink);font-size:11.5px;line-height:1.35}
.icon{position:absolute;width:12px;height:12px}
.quote{position:absolute;font-family:"Alegreya",Georgia,serif;font-style:italic;font-weight:700;color:var(--sky);font-size:19px}
.creds{position:absolute;left:0;width:100%;text-align:center;color:var(--white);font-size:11px}
.creds__rule{position:absolute;left:90px;width:336px;height:1px;background:rgba(255,255,255,.7);top:193px}
.brand--back{left:0;width:100%;top:38px;text-align:center;font-size:16px;color:#cfe7f5}
.emblem{position:absolute;left:-60px;top:10px;width:300px;height:300px;border-radius:50%;background:radial-gradient(circle at 60% 40%,#fdf7c2,#f6ea6a 55%,#e6f2fa 56%,#e6f2fa)}
.emblem__text{position:absolute;left:150px;top:90px;font-style:italic;font-weight:700;color:var(--ink);font-size:14px;line-height:1.35;text-align:center}
.brand--d{right:62px;top:28px;color:var(--ink);font-size:15px;text-align:right}
.footband{position:absolute;left:0;bottom:0;width:100%;height:28px;background:var(--deep);color:var(--white);font-weight:600;font-size:12.5px;text-align:center;line-height:28px}
</style>
</head>
<body>

<!-- back -->
<section class="card card--back">
  <div class="brand brand--back"><span class="brand__dot"></span>Evergreen Years</div>
  <p class="creds" style="top:112px">B.A. ( Soc.) Dip. Ed. (Sec.) Wellness Coach, Cert. 4 Personal Trainer</p>
  <div class="creds__rule" style="top:135px"></div>
  <p class="creds" style="top:146px;font-size:10.5px">Cert. Nutritition MOVE ON Facilitator, Ageing Well Moving Freely Facilitator, NLP Master</p>
</section>

<!-- front A -->
<section class="card card--a">
  <svg class="swoosh" viewBox="0 0 514 284" aria-hidden="true">
    <path d="M0 0H292C336 80 322 220 30 284H0Z" fill="var(--sun)"/>
    <path d="M0 0H284C326 80 312 216 14 284H0Z" fill="var(--navy)"/>
    <path d="M0 0H228C280 100 240 215 0 275Z" fill="var(--sky)"/>
  </svg>
  <div class="brand brand--front"><span class="brand__dot"></span>Evergreen Years<br><span class="brand__sub">Nutrition &amp; Fitness</span></div>
  <p class="tagline" style="right:32px;top:12px">For Seniors by a Senior</p>
  <p class="addr" style="right:33px;top:40px">Private gym at:<br>17 Fennick Street, Brantwood,<br>Perth, WA 6291</p>
  <svg class="icon" style="right:16px;top:52px" viewBox="0 0 12 12"><path d="M6 0a4 4 0 0 1 4 4c0 3-4 8-4 8S2 7 2 4a4 4 0 0 1 4-4z" fill="var(--sky)"/><circle cx="6" cy="4" r="1.5" fill="#fff"/></svg>
  <h2 class="name" style="right:20px;top:116px">Corinne Dalby</h2>
  <p class="role" style="right:20px;top:148px">Nutrition &amp; Fitness Coach<br>for Seniors</p>
  <div class="rule" style="left:296px;width:168px;top:213px"></div>
  <p class="contact" style="right:39px;top:238px">0412736158<br>corinnedalby@fernpost.example</p>
  <svg class="icon" style="right:18px;top:240px" viewBox="0 0 12 12"><path d="M2 1l2 0 1 3-1.5 1a7 7 0 0 0 3.5 3.5L8 7l3 1v2a1 1 0 0 1-1 1C5 11 1 7 1 2a1 1 0 0 1 1-1z" fill="var(--ink)"/></svg>
  <svg class="icon" style="right:18px;top:256px" viewBox="0 0 12 12"><rect x="0.5" y="2" width="11" height="8" fill="var(--ink)"/><path d="M1 2.5l5 4 5-4" stroke="#fff" fill="none"/></svg>
</section>

<!-- front B -->
<section class="card card--b">
  <svg class="swoosh" viewBox="0 0 514 284" aria-hidden="true">
    <path d="M0 0H292C336 80 322 220 30 284H0Z" fill="var(--sun)"/>
    <path d="M0 0H284C326 80 312 216 14 284H0Z" fill="var(--navy)"/>
    <path d="M0 0H228C280 100 240 215 0 275Z" fill="var(--sky)"/>
  </svg>
  <div class="brand brand--front"><span class="brand__dot"></span>Evergreen Years<br><span class="brand__sub">Nutrition &amp; Fitness</span></div>
  <h2 class="name" style="right:24px;top:6px">Corinne Dalby</h2>
  <p class="role" style="right:24px;top:40px;font-size:11.5px">Nutrition &amp; Fitness Coach<br>for Seniors</p>
  <div class="rule" style="left:324px;width:168px;top:94px"></div>
  <p class="contact" style="right:40px;top:114px">0412736158<br>corinnedalby@fernpost.example</p>
  <svg class="icon" style="right:22px;top:116px" viewBox="0 0 12 12"><path d="M2 1l2 0 1 3-1.5 1a7 7 0 0 0 3.5 3.5L8 7l3 1v2a1 1 0 0 1-1 1C5 11 1 7 1 2a1 1 0 0 1 1-1z" fill="var(--ink)"/></svg>
  <svg class="icon" style="right:22px;top:132px" viewBox="0 0 12 12"><rect x="0.5" y="2" width="11" height="8" fill="var(--ink)"/><path d="M1 2.5l5 4 5-4" stroke="#fff" fill="none"/></svg>
  <p class="addr" style="right:46px;top:150px">Private gym at:<br>17 Fennick Street, Brantwood,<br>Perth, WA 6291</p>
  <svg class="icon" style="right:26px;top:164px" viewBox="0 0 12 12"><path d="M6 0a4 4 0 0 1 4 4c0 3-4 8-4 8S2 7 2 4a4 4 0 0 1 4-4z" fill="var(--sky)"/><circle cx="6" cy="4" r="1.5" fill="#fff"/></svg>
  <p class="quote" style="right:28px;top:242px">“For Seniors by a Senior”</p>
</section>

<!-- front C -->
<section class="card card--c">
  <svg class="swoosh" viewBox="0 0 514 284" aria-hidden="true">
    <path d="M0 0H292C336 80 322 220 30 284H0Z" fill="var(--sun)"/>
    <path d="M0 0H284C326 80 312 216 14 284H0Z" fill="var(--navy)"/>
    <path d="M0 0H228C280 100 240 215 0 275Z" fill="var(--sky)"/>
  </svg>
  <div class="brand brand--front"><span class="brand__dot"></span>Evergreen Years<br><span class="brand__sub">Nutrition &amp; Fitness</span></div>
  <p class="tagline" style="right:32px;top:12px">For Seniors by a Senior</p>
  <p class="addr" style="right:33px;top:40px">Private gym at:<br>17 Fennick Street, Brantwood,<br>Perth, WA 6291</p>
  <svg class="icon" style="right:16px;top:54px" viewBox="0 0 12 12"><path d="M6 0a4 4 0 0 1 4 4c0 3-4 8-4 8S2 7 2 4a4 4 0 0 1 4-4z" fill="var(--sky)"/><circle cx="6" cy="4" r="1.5" fill="#fff"/></svg>
  <p class="contact" style="right:33px;top:88px">0412736158<br>corinnedalby@fernpost.example</p>
  <svg class="icon" style="right:16px;top:90px" viewBox="0 0 12 12"><path d="M2 1l2 0 1 3-1.5 1a7 7 0 0 0 3.5 3.5L8 7l3 1v2a1 1 0 0 1-1 1C5 11 1 7 1 2a1 1 0 0 1 1-1z" fill="var(--ink)"/></svg>
  <svg class="icon" style="right:16px;top:106px" viewBox="0 0 12 12"><rect x="0.5" y="2" width="11" height="8" fill="var(--ink)"/><path d="M1 2.5l5 4 5-4" stroke="#fff" fill="none"/></svg>
  <div class="rule" style="left:296px;width:168px;top:153px"></div>
  <h2 class="name" style="right:32px;top:186px">Corinne Dalby</h2>
  <p class="role" style="right:32px;top:220px">Nutrition &amp; Fitness Coach for Seniors</p>
</section>

<!-- front D -->
<section class="card card--d">
  <div class="emblem" role="img" aria-label="Large decorative brand emblem in blue and yellow"></div>
  <p class="emblem__text">For Seniors<br>by a Senior</p>
  <div class="brand brand--d"><span class="brand__dot"></span>Evergreen Years<br>Nutrition &amp; Fitness</div>
  <h2 class="name" style="right:40px;top:120px">Corinne Dalby</h2>
  <p class="role" style="right:40px;top:152px">Nutrition &amp; Fitness Coach for Seniors</p>
  <p class="addr" style="right:40px;top:198px;color:var(--ink)">Private gym at:<br>17 Fennick Street, Brantwood, Perth, WA 6291</p>
  <div class="footband">0412736158 &nbsp;&nbsp;| &nbsp;&nbsp;corinnedalby@fernpost.example</div>
</section>

</body>
</html>
```